We are an appraisal and dispute resolution company that works with insurance companies and insureds.

We need a website built that appeals to insurance companies as well as insureds to entrust we can assist come to a resolution with their property insurance claim.

Target Market(s)

Insurance Carriers and Insureds

Industry/Entity Type

Insurance

Coding

Coded - Design and coding required

Number of Pages Required

5+ page

Requirements
Must have
• Would like to click on pages and it take you down one page to that specific section
Nice to have
• Clean look

```html
<!DOCTYPE html>
<html lang="en">
<head>
<meta charset="utf-8">
<title>Keystone – Appraisal and Dispute Resolution</title>
<link rel="stylesheet" href="https://fonts.googleapis.com/css2?family=Archivo:wght@400;500;600;700&family=Lato:wght@400;700&display=swap">
<style>
:root{
  --teal:#1fb5b6;
  --navy:#15213a;
  --ink:#1d1d1f;
  --muted:#555b63;
  --mist:#e8f0f0;
  --white:#ffffff;
}
*{margin:0;padding:0;box-sizing:border-box}
html,body{width:1200px;height:3963px;overflow:hidden}
body{position:relative;font-family:'Lato',sans-serif;color:var(--ink);background:var(--white)}
.abs{position:absolute}
h2.section-title{position:absolute;left:0;width:1200px;text-align:center;font-family:'Archivo',sans-serif;font-weight:600;font-size:34px;color:var(--ink)}
h2 .accent{color:var(--teal)}
.underline{position:absolute;height:4px;width:62px;background:var(--teal)}

/* hero */
.hero{left:0;top:0;width:1200px;height:736px;background:linear-gradient(120deg,#3a3430 0%,#6f5f52 40%,#a89886 70%,#d8cfc3 100%)}
.hero-shade{left:0;top:0;width:1200px;height:736px;background:linear-gradient(180deg,rgba(0,0,0,.55),rgba(0,0,0,.15) 60%,rgba(0,0,0,.3))}
.brand{left:131px;top:24px;color:#fff;font-family:'Archivo',sans-serif;font-weight:600;font-size:28px;letter-spacing:1px}
.nav{top:30px;font-family:'Archivo',sans-serif;font-size:14px;color:#fff;font-weight:500}
.nav.active{color:var(--teal)}
.nav-bar{left:381px;top:58px;width:34px;height:2px;background:var(--teal)}
.welcome{left:0;width:1200px;top:196px;text-align:center;color:#fff;font-size:20px;letter-spacing:6px}
.hero-title{left:0;width:1200px;top:226px;text-align:center;color:#fff;font-family:'Archivo',sans-serif;font-weight:700;font-size:52px;line-height:48px;letter-spacing:1px}
.btn{background:var(--teal);color:#fff;font-family:'Archivo',sans-serif;font-weight:600;font-size:14px;border-radius:24px;text-align:center}
.hero-btn{left:494px;top:343px;width:180px;height:43px;line-height:43px}
.arrow{top:365px}

/* about */
.about-card{left:524px;top:806px;width:576px;height:428px;background:#fff;box-shadow:0 10px 40px rgba(0,0,0,.1)}
.about-img{left:112px;top:872px;width:502px;height:391px;border-radius:70px 0 70px 0;background:linear-gradient(135deg,#bfb7ac,#8a7a6a 55%,#d9d2c9)}
.about-title{left:664px;top:880px;font-family:'Archivo',sans-serif;font-weight:600;font-size:34px}
.about-text{left:664px;top:956px;width:384px;font-size:14px;line-height:24.5px;color:#333}

/* what we do */
.wwd{left:0;top:1370px;width:1200px;height:480px;background:linear-gradient(90deg,#1a2a44,#24364f 50%,#1b2b45)}
.wwd-text{left:300px;width:600px;top:1506px;text-align:center;color:#e6ecf2;font-size:15px;line-height:25px}
.svc{top:1632px;width:308px;height:381px;background:#fff;box-shadow:0 8px 24px rgba(0,0,0,.08)}
.svc-img{left:0;top:0;width:308px;height:214px}
.svc-icon{left:34px;top:190px;width:52px;height:52px;border-radius:50%}
.svc h3{position:absolute;left:30px;top:260px;font-family:'Archivo',sans-serif;font-weight:600;font-size:19px}
.svc p{position:absolute;left:30px;top:293px;width:240px;font-size:12.5px;line-height:19.5px;color:#666}

/* why */
.why{left:0;top:1850px;width:1200px;height:748px;background:var(--mist)}
.why-circle{top:2288px;width:100px;height:100px;border-radius:50%;display:flex;align-items:center;justify-content:center}
.why-circle.teal{background:var(--teal);box-shadow:0 0 0 4px var(--mist),0 0 0 6px var(--teal)}
.why-circle.navy{background:var(--navy);box-shadow:0 0 0 4px var(--mist),0 0 0 6px var(--navy)}
.why-title{top:2412px;width:260px;text-align:center;font-family:'Archivo',sans-serif;font-weight:500;font-size:18px}
.why-text{top:2444px;width:230px;text-align:center;font-size:13px;line-height:19px;color:#333}

/* testimonials */
.quote-card{top:2764px;width:462px;height:310px;border:1.5px solid #d5d8db;background:#fff}
.quote-img{left:0;top:0;width:172px;height:307px}
.quote-mark{left:197px;top:30px;color:#c9ccd0;font-family:'Archivo',sans-serif;font-size:36px;font-weight:700}
.quote-lead{left:197px;top:68px;width:240px;font-size:15.5px;line-height:22px;color:#222}
.quote-body{left:197px;top:122px;width:240px;font-size:12.5px;line-height:22px;color:#444}
.quote-name{left:197px;top:240px;font-size:12.5px;font-weight:700}
.quote-city{left:197px;top:260px;font-size:10px;color:#555}
.dot{top:3123px;width:11px;height:11px;border-radius:50%;background:var(--navy)}

/* contact */
.contact{left:0;top:3207px;width:1200px;height:612px;background:linear-gradient(180deg,#1fb3b4 0%,#23b6b7 60%,#1aa5a8 100%)}
.contact-card{left:111px;top:3296px;width:990px;height:428px;background:#fff;border-radius:22px;overflow:hidden}
.form-panel{left:395px;top:0;width:595px;height:428px;background:var(--navy);border-radius:40px 0 0 100px}
.c-title{left:180px;top:3372px;font-family:'Archivo',sans-serif;font-weight:600;font-size:30px}
.c-sub{left:180px;top:3414px;font-size:14px;color:#444}
.c-ring{width:68px;height:68px;border-radius:50%;border:1.5px solid #333;display:flex;align-items:center;justify-content:center}
.c-label{font-family:'Archivo',sans-serif;font-size:14px;font-weight:500}
.c-value{font-size:19px;font-weight:700}
.field{font-size:13px;color:#fff}
.field-line{height:2px;background:#d6dde6}
.send{left:871px;top:3622px;width:157px;height:44px;line-height:44px}

/* footer */
.foot-brand{left:133px;top:3866px;font-family:'Archivo',sans-serif;font-weight:600;font-size:24px;color:var(--navy);letter-spacing:1px}
.foot-link{top:3868px;font-family:'Archivo',sans-serif;font-weight:500;font-size:14px;color:var(--ink)}
.copy{left:354px;top:3900px;font-size:11.5px;color:#777}
</style>
</head>
<body>

<header>
  <div class="abs hero" role="img" aria-label="Photo of a couple reviewing documents with an advisor"></div>
  <div class="abs hero-shade"></div>
  <div class="abs brand">KEYSTONE</div>
  <nav>
    <div class="abs nav active" style="left:366px">ABOUT US</div>
    <div class="abs nav-bar"></div>
    <div class="abs nav" style="left:498px">OUR SERVICES</div>
    <div class="abs nav" style="left:660px">WHY CHOOSE US</div>
    <div class="abs nav" style="left:840px">TESTIMONIALS</div>
    <div class="abs nav" style="left:1001px">CONTACT US</div>
  </nav>
  <div class="abs welcome">WELCOME TO KEYSTONE</div>
  <h1 class="abs hero-title">KEYSTONE APPRAISAL AND<br>DISPUTE RESOLUTION</h1>
  <div class="abs btn hero-btn">CONTACT US</div>
  <svg class="abs arrow" style="left:20px" width="26" height="40" viewBox="0 0 26 40"><path d="M22 3 L5 20 L22 37" fill="none" stroke="#fff" stroke-width="4"/></svg>
  <svg class="abs arrow" style="left:1136px" width="26" height="40" viewBox="0 0 26 40"><path d="M4 3 L21 20 L4 37" fill="none" stroke="#fff" stroke-width="4"/></svg>
</header>

<section class="about">
  <div class="abs" style="left:517px;top:800px;width:246px;height:5px;background:var(--teal)"></div>
  <div class="abs" style="left:517px;top:800px;width:5px;height:72px;background:var(--teal)"></div>
  <div class="abs" style="left:1101px;top:1002px;width:6px;height:233px;background:var(--teal)"></div>
  <div class="abs" style="left:843px;top:1229px;width:264px;height:6px;background:var(--teal)"></div>
  <div class="abs about-card"></div>
  <div class="abs about-img" role="img" aria-label="Photo of a smiling family sitting together at home"></div>
  <h2 class="abs about-title">ABOUT <span style="color:var(--teal)">KEYSTONE</span></h2>
  <div class="underline" style="left:664px;top:928px"></div>
  <p class="abs about-text">Lorem Ipsum is simply dummy text of the printing and typesetting industry. Lorem Ipsum has been the industry's standard dummy text ever since the 1500s, when an unknown printer took a galley of type and scrambled it to make a type specimen Lorem Ipsum is simply dummy text of the printing and typesetting industry. Lorem Ipsum has been the industry's standard dummy text ever since the 1500s, when an unknow</p>
</section>

<section class="what-we-do">
  <div class="abs wwd" role="img" aria-label="Dimmed photo of a business meeting"></div>
  <h2 class="section-title" style="top:1438px;color:#fff">WHAT <span class="accent">WE DO</span></h2>
  <div class="underline" style="left:569px;top:1484px"></div>
  <p class="abs wwd-text">Lorem Ipsum is simply dummy text of the printing and typesetting industry. Lorem Ipsum has been the industry's standard dummy text ever</p>

  <article class="abs svc" style="left:120px">
    <div class="abs svc-img" role="img" aria-label="Photo of consultants working at a desk" style="background:linear-gradient(135deg,#c9d3da,#7d8c98)"></div>
    <div class="abs svc-icon" style="background:var(--teal)"><svg width="52" height="52" viewBox="0 0 52 52"><circle cx="26" cy="22" r="7" fill="none" stroke="#fff" stroke-width="2"/><path d="M15 37 q11-12 22 0" fill="none" stroke="#fff" stroke-width="2"/></svg></div>
    <h3>CONSULTING</h3>
    <p>Lorem Ipsum is simply dummy text of the printing and typesetting industry. Lorem Ipsum has been the industry's</p>
  </article>
  <article class="abs svc" style="left:446px">
    <div class="abs svc-img" role="img" aria-label="Photo of a handshake over a model house" style="background:linear-gradient(135deg,#b7a894,#5e5144)"></div>
    <div class="abs svc-icon" style="background:var(--navy)"><svg width="52" height="52" viewBox="0 0 52 52"><circle cx="19" cy="25" r="4" fill="none" stroke="#fff" stroke-width="2"/><circle cx="33" cy="25" r="4" fill="none" stroke="#fff" stroke-width="2"/><path d="M12 37 q7-8 14 0 q7-8 14 0" fill="none" stroke="#fff" stroke-width="2"/><rect x="21" y="12" width="10" height="7" fill="none" stroke="#fff" stroke-width="1.6"/></svg></div>
    <h3>DISPUTE RESOLUTION</h3>
    <p>Lorem Ipsum is simply dummy text of the printing and typesetting industry. Lorem Ipsum has been the industry's</p>
  </article>
  <article class="abs svc" style="left:780px">
    <div class="abs svc-img" role="img" aria-label="Photo of a couple reviewing paperwork" style="background:linear-gradient(135deg,#d6d9dc,#6f6458)"></div>
    <div class="abs svc-icon" style="background:var(--teal)"><svg width="52" height="52" viewBox="0 0 52 52"><rect x="17" y="14" width="16" height="22" fill="none" stroke="#fff" stroke-width="2"/><path d="M21 20h8M21 25h8M21 30h5" stroke="#fff" stroke-width="1.6"/><circle cx="34" cy="34" r="4" fill="none" stroke="#fff" stroke-width="2"/></svg></div>
    <h3>APPRAISAL</h3>
    <p>Lorem Ipsum is simply dummy text of the printing and typesetting industry. Lorem Ipsum has been the industry's</p>
  </article>
</section>

<section class="why-choose">
  <div class="abs why" style="z-index:-1"></div>
  <h2 class="section-title" style="top:2098px">WHY CHOOSE <span class="accent">KEYSTONE</span></h2>
  <div class="underline" style="left:564px;top:2148px;width:84px"></div>
  <svg class="abs" style="left:300px;top:2180px" width="600" height="110" viewBox="0 0 600 110">
    <g fill="none" stroke="#b9c2cc" stroke-width="2">
      <path d="M292 6 V28 q0 12 -12 12 H32 q-14 0 -14 14 V94"/>
      <path d="M308 6 V28 q0 12 12 12 H570 q14 0 14 14 V94"/>
      <path d="M300 6 V92"/>
    </g>
    <circle cx="18" cy="96" r="4.5" fill="var(--teal)"/>
    <circle cx="300" cy="96" r="4.5" fill="var(--navy)"/>
    <circle cx="584" cy="96" r="4.5" fill="var(--teal)"/>
  </svg>
  <div class="abs why-circle teal" style="left:268px"><svg width="40" height="40" viewBox="0 0 40 40"><path d="M12 34v-8a11 11 0 1 1 16-9l3 6h-4v6h-6v5" fill="none" stroke="#fff" stroke-width="2"/><circle cx="22" cy="16" r="3" fill="none" stroke="#fff" stroke-width="2"/></svg></div>
  <div class="abs why-circle navy" style="left:553px"><svg width="40" height="40" viewBox="0 0 40 40"><rect x="6" y="13" width="28" height="20" rx="2" fill="none" stroke="#fff" stroke-width="2"/><path d="M15 13v-4h10v4M6 21h28M18 21v3h4v-3" fill="none" stroke="#fff" stroke-width="2"/></svg></div>
  <div class="abs why-circle teal" style="left:837px"><svg width="40" height="40" viewBox="0 0 40 40"><path d="M14 26a10 10 0 1 1 12 0v5H14z" fill="none" stroke="#fff" stroke-width="2"/><path d="M16 35h8M20 14v12M16 18l4 4 4-4" fill="none" stroke="#fff" stroke-width="2"/></svg></div>
  <div class="abs why-title" style="left:188px">LOREM IPSUM</div>
  <div class="abs why-title" style="left:478px">LOREM IPSUM</div>
  <div class="abs why-title" style="left:760px">LOREM IPSUM</div>
  <p class="abs why-text" style="left:203px">Lorem Ipsum is simply dummy text of the printing and typesetting industry. Lorem Ipsum</p>
  <p class="abs why-text" style="left:492px">Lorem Ipsum is simply dummy text of the printing and typesetting industry. Lorem Ipsum</p>
  <p class="abs why-text" style="left:781px">Lorem Ipsum is simply dummy text of the printing and typesetting industry. Lorem Ipsum</p>
</section>

<section class="testimonials">
  <h2 class="section-title" style="top:2662px">WHAT OUR CLIENT SAYS</h2>
  <div class="underline" style="left:572px;top:2712px;width:68px"></div>
  <article class="abs quote-card" style="left:131px">
    <div class="abs quote-img" role="img" aria-label="Portrait photo of a client" style="background:linear-gradient(160deg,#c9b9a6,#a9bdd0)"></div>
    <div class="abs quote-mark">“</div>
    <p class="abs quote-lead">“Lorem ipsum dolor sit amet, cons ectetur adipiscing elit”</p>
    <p class="abs quote-body">“Lorem ipsum dolor sit amet, consectetur adipiscing elit. In congue velit quis augue facilisis malesuada. Nulla facilisi. Praesent laoreet ligula odio, et sagittis metus maximus ver.”</p>
    <div class="abs quote-name">Helen R. Marsh</div>
    <div class="abs quote-city">London, UK</div>
  </article>
  <article class="abs quote-card" style="left:634px">
    <div class="abs quote-img" role="img" aria-label="Portrait photo of a client" style="background:linear-gradient(160deg,#d9cfc4,#e8c8b8)"></div>
    <div class="abs quote-mark">“</div>
    <p class="abs quote-lead">“Lorem ipsum dolor sit amet, cons ectetur adipiscing elit”</p>
    <p class="abs quote-body">“Lorem ipsum dolor sit amet, consectetur adipiscing elit. In congue velit quis augue facilisis malesuada. Nulla facilisi. Praesent laoreet ligula odio, et sagittis metus maximus ver.”</p>
    <div class="abs quote-name">Claire D. Benton</div>
    <div class="abs quote-city">London, UK</div>
  </article>
  <div class="abs dot" style="left:580px;background:var(--teal)"></div>
  <div class="abs dot" style="left:601px"></div>
  <div class="abs dot" style="left:622px"></div>
</section>

<section class="contact-section">
  <div class="abs contact" role="img" aria-label="Teal background with a soft dotted wave texture"></div>
  <div class="abs contact-card">
    <div class="abs form-panel"></div>
  </div>
  <h2 class="abs c-title">CONTACT <span style="color:var(--teal)">US</span></h2>
  <p class="abs c-sub">Please contact us on the below details.</p>
  <div class="abs c-ring" style="left:178px;top:3470px"><svg width="34" height="34" viewBox="0 0 34 34"><path d="M8 5l5 1 2 6-3 2q3 6 8 8l2-3 6 2 1 5q-2 4-6 3Q10 27 5 11Q4 7 8 5z" fill="none" stroke="var(--teal)" stroke-width="1.8"/></svg></div>
  <div class="abs c-label" style="left:273px;top:3477px">PHONE NUMBER</div>
  <div class="abs c-value" style="left:273px;top:3498px">(+123) 555 0199</div>
  <div class="abs c-ring" style="left:178px;top:3571px"><svg width="34" height="34" viewBox="0 0 34 34"><rect x="4" y="8" width="26" height="18" fill="none" stroke="var(--teal)" stroke-width="1.8"/><path d="M4 8l13 10 13-10M4 26l10-9M30 26l-10-9" fill="none" stroke="var(--teal)" stroke-width="1.8"/></svg></div>
  <div class="abs c-label" style="left:279px;top:3578px">EMAIL US</div>
  <div class="abs" style="left:279px;top:3602px;font-size:14px">enquiry@keystone-example.com</div>

  <div class="abs field" style="left:575px;top:3376px">First Name</div>
  <div class="abs field-line" style="left:573px;top:3403px;width:211px"></div>
  <div class="abs field" style="left:808px;top:3376px">Last Name</div>
  <div class="abs field-line" style="left:806px;top:3403px;width:214px"></div>
  <div class="abs field" style="left:575px;top:3449px">E-mail address</div>
  <div class="abs field-line" style="left:573px;top:3476px;width:211px"></div>
  <div class="abs field" style="left:808px;top:3449px">Phone</div>
  <div class="abs field-line" style="left:806px;top:3476px;width:214px"></div>
  <div class="abs field" style="left:575px;top:3528px">Message</div>
  <div class="abs field-line" style="left:573px;top:3580px;width:447px"></div>
  <div class="abs btn send">SEND MESSAGE</div>
</section>

<footer>
  <div class="abs foot-brand">KEYSTONE</div>
  <div class="abs foot-link" style="left:354px">HOME</div>
  <div class="abs foot-link" style="left:448px">ABOUT</div>
  <div class="abs foot-link" style="left:549px">OUR SERVICES</div>
  <div class="abs foot-link" style="left:703px">WHY US?</div>
  <div class="abs foot-link" style="left:819px">BLOG</div>
  <div class="abs foot-link" style="left:909px">CONTACT US</div>
  <div class="abs copy">Copyright 2021 Keystone All Right Rserverd</div>
</footer>

</body>
</html>
```